Music Industry Business Needs a Business Card Design

Copper Lantern is an audio mastering company that has been in business for 20 years. Mastering is the final creative step in the music production chain. Our job is to make the music sound as good as it possibly can prior to release to the public. Our world is technical, artistic, precise. We work on everything from independent artists to the music for the Grandfield Cup. We are looking for a new, more modern business card design. I am uploading a copy of our logo, although it doesn't absolutely need to be included in the design.

Target Market(s)

Music Industry Professionals

Industry/Entity Type

Business

Contact Information for Business Card

Address, Phone, Email, Website, Name, Job Title

Font styles to use
Sans Serif

Requirements
Must have
• Sorry, but I don't have any concrete things to request. If I had a clear idea of what I want, I would probably just design something myself. I am looking for fresh input and thought I would try this.
Should not have
• Anything that is typical, such as headphones or the like.

```html
<!DOCTYPE html>
<html lang="en">
<head>
<meta charset="utf-8">
<title>Copper Lantern – Business Card</title>
<link href="https://fonts.googleapis.com/css2?family=Open+Sans:wght@400&family=Arimo:wght@400&display=swap" rel="stylesheet">
<style>
  :root {
    --backdrop: #d9d5d0;
    --card-light: #f3f3f2;
    --card-dark: #343434;
    --ink: #111111;
    --ink-soft: #555555;
    --rule: #5a5a5a;
    --tab-dark: #2e2e2e;
    --tab-light: #e9e9e9;
    --paper-white: #ffffff;
  }
  * { margin: 0; padding: 0; box-sizing: border-box; }
  html, body {
    width: 1080px;
    height: 1200px;
    overflow: hidden;
    background: var(--backdrop);
  }
  .canvas {
    position: relative;
    width: 1080px;
    height: 1200px;
  }
  .card {
    position: absolute;
    box-shadow: 0 4px 14px rgba(0,0,0,0.25);
    overflow: hidden;
  }
  .card-front {
    left: 135px; top: 86px;
    width: 841px; height: 480px;
    background: var(--card-light);
  }
  .card-back {
    left: 138px; top: 661px;
    width: 839px; height: 478px;
    background: var(--card-dark);
  }
  .edge-tabs {
    position: absolute;
    inset: 0;
    width: 100%;
    height: 100%;
  }
  .brand-name {
    position: absolute;
    font-family: "Open Sans", sans-serif;
    font-weight: 400;
    white-space: nowrap;
    line-height: 1;
  }
  .card-front .brand-name {
    left: 97px; top: 98px;
    font-size: 30px;
    color: var(--ink);
  }
  .card-back .brand-name {
    left: 445px; top: 182px;
    transform: translateX(-50%);
    font-size: 58px;
    color: var(--paper-white);
  }
  .name-rule {
    position: absolute;
    top: 229px;
    height: 3px;
    background: var(--rule);
  }
  .name-rule.left { left: 0; width: 50px; }
  .name-rule.right { left: 375px; right: 0; }
  .details {
    font-family: "Arimo", sans-serif;
    color: var(--ink-soft);
    white-space: nowrap;
    line-height: 1;
  }
  .holder-name {
    position: absolute;
    left: 71px; top: 220px;
    font-size: 20px;
  }
  .holder-title {
    position: absolute;
    right: 486px; top: 247px;
    font-size: 16px;
  }
  .address {
    position: absolute;
    left: 71px; top: 291px;
    font-size: 17px;
  }
  .contact {
    position: absolute;
    display: flex;
    align-items: center;
    gap: 17px;
    font-size: 19px;
  }
  .contact .icon {
    width: 30px; height: 30px;
    background: var(--ink-soft);
    display: flex;
    align-items: center;
    justify-content: center;
  }
  .contact .icon svg { width: 20px; height: 20px; }
  .contact.mobile { left: 73px; top: 345px; }
  .contact.phone { left: 73px; top: 398px; }
  .contact.web { left: 477px; top: 345px; }
  .contact.mail { left: 477px; top: 398px; }
  .web-address {
    position: absolute;
    left: 421px; top: 420px;
    transform: translateX(-50%);
    font-family: "Arimo", sans-serif;
    font-size: 30px;
    letter-spacing: 5px;
    color: var(--paper-white);
    white-space: nowrap;
    line-height: 1;
  }
</style>
</head>
<body>
<main class="canvas">

  <section class="card card-front" aria-label="Business card front">
    <svg class="edge-tabs" viewBox="0 0 841 480" aria-hidden="true">
      <polygon points="841,18 822,38 822,128 841,148" fill="var(--tab-dark)"/>
      <polygon points="0,320 19,340 19,432 0,452" fill="var(--tab-dark)"/>
    </svg>

    <div class="brand-name">COPPER LANTERN</div>

    <div class="name-rule left"></div>
    <div class="name-rule right"></div>
    <div class="holder-name details">XXXXXX-NAME-XXXXXXX</div>
    <div class="holder-title details">DESIGNATION</div>

    <div class="address details">XXADDRESSXX, XXXXXXXXXXXXXXXXXX, XXXXXXXXXXXXX</div>

    <div class="contact mobile details">
      <span class="icon"><svg viewBox="0 0 20 20"><rect x="6" y="2" width="8" height="16" rx="1.5" fill="none" stroke="#fff" stroke-width="1.6"/><circle cx="10" cy="15.5" r="0.9" fill="#fff"/></svg></span>
      <span>XXXXXXXXXXXXXXXXXX</span>
    </div>
    <div class="contact phone details">
      <span class="icon"><svg viewBox="0 0 20 20"><path d="M5 3 L8 3 L9 7 L7 8.5 C8 11 9.5 12.5 12 13.5 L13.5 11.5 L17 12.5 L17 15.5 C17 16.5 16 17 15 17 C9 16.5 3.5 11 3 5 C3 4 4 3 5 3 Z" fill="#fff"/></svg></span>
      <span>XXXXXXXXXXXXXXXXX</span>
    </div>
    <div class="contact web details">
      <span class="icon"><svg viewBox="0 0 20 20" fill="none" stroke="#fff" stroke-width="1.3"><circle cx="10" cy="10" r="7"/><ellipse cx="10" cy="10" rx="3" ry="7"/><line x1="3" y1="10" x2="17" y2="10"/><line x1="4.5" y1="6" x2="15.5" y2="6"/><line x1="4.5" y1="14" x2="15.5" y2="14"/></svg></span>
      <span>XXXXXXXXXXXXXXXXXX</span>
    </div>
    <div class="contact mail details">
      <span class="icon"><svg viewBox="0 0 20 20" fill="none" stroke="#fff" stroke-width="1.5"><rect x="3" y="5" width="14" height="10"/><polyline points="3,5 10,11 17,5"/></svg></span>
      <span>XXXXXXXXXXXXXXXXXX</span>
    </div>
  </section>

  <section class="card card-back" aria-label="Business card back">
    <svg class="edge-tabs" viewBox="0 0 839 478" aria-hidden="true">
      <polygon points="839,23 820,43 820,131 839,151" fill="var(--tab-light)"/>
      <polygon points="0,331 19,351 19,437 0,457" fill="var(--tab-light)"/>
    </svg>

    <div class="brand-name">COPPER LANTERN</div>
    <div class="web-address">www.urwebaddress.com</div>
  </section>

</main>
</body>
</html>
```